Business Card Design Project

I have just chosen a logo and would now like this designed onto a business card for my hair salon. I would like it to be classy not to busy and have a wow factor when people look at them
Has to Include on card:
Logo Design
And business details below
Kellie-ann Drummond (owner)
0482 736 219
Rdw@vomblet.com.au
71 Willowmere Rise Corvin Cove
Logo is now attached please provide designs
Hair

```html
<!DOCTYPE html>
<html lang="en">
<head>
<meta charset="utf-8">
<title>Lustre Hair Atelier – Business Cards</title>
<link rel="stylesheet" href="https://fonts.googleapis.com/css2?family=Red+Hat+Display:wght@500;700&family=Pacifico&family=Gelasio:wght@500;700&display=swap">
<style>
  :root {
    --ink: #111111;
    --text-grey: #3d3d3d;
    --brand-pink: #e0157a;
    --brand-teal: #3ab3c3;
    --back-pink: #d8266f;
    --paper: #ffffff;
    --page: #ffffff;
  }
  * { margin: 0; padding: 0; box-sizing: border-box; }
  html, body { width: 1200px; height: 900px; overflow: hidden; background: var(--page); }
  .board { position: relative; width: 1200px; height: 900px; font-family: "Red Hat Display", Arial, sans-serif; color: var(--ink); }

  .board-title { position: absolute; left: 20px; top: 21px; font-size: 21px; font-weight: 700; letter-spacing: 0.2px; line-height: 1; }
  .board-subtitle { position: absolute; left: 20px; top: 45px; font-size: 14px; font-weight: 500; line-height: 1; }

  .side-label { position: absolute; left: 349px; font-size: 12.5px; font-weight: 500; line-height: 1; }
  .side-label--front { top: 129px; }
  .side-label--back { top: 471px; }

  .card { position: absolute; left: 349px; width: 440px; height: 245px; box-shadow: 0 1px 4px rgba(0,0,0,0.35); }
  .card--front { top: 178px; background: var(--paper); }
  .card--back { top: 505px; height: 244px; background: var(--back-pink); }

  .card-frame { position: absolute; left: 23px; top: 24px; width: 397px; height: 196px; border: 1px dotted var(--brand-pink); }

  .brand-mark { position: absolute; left: 147px; top: 10px; width: 146px; height: 60px; background: var(--paper); text-align: center; font-family: "Gelasio", Georgia, serif; font-weight: 500; color: var(--brand-pink); line-height: 1; }
  .brand-mark__main { display: block; font-size: 24px; letter-spacing: 1px; padding-top: 2px; }
  .brand-mark__sub { display: block; font-size: 15px; letter-spacing: 0.5px; margin-top: 4px; }

  .contact { position: absolute; left: 0; width: 440px; text-align: center; }
  .contact__name { top: 96px; font-family: "Pacifico", cursive; font-size: 21px; color: var(--brand-teal); line-height: 1.2; }
  .contact__phone { top: 137px; font-family: "Gelasio", Georgia, serif; font-weight: 700; font-size: 15px; letter-spacing: 0.5px; color: var(--ink); }
  .contact__details { top: 163px; font-family: "Gelasio", Georgia, serif; font-weight: 500; font-size: 12px; line-height: 15px; color: var(--text-grey); }
</style>
</head>
<body>
<main class="board">
  <h1 class="board-title">LUSTRE HAIR ATELIER</h1>
  <p class="board-subtitle">BUSINESS CARDS</p>

  <p class="side-label side-label--front">FRONT</p>
  <section class="card card--front" aria-label="Business card front">
    <div class="card-frame"></div>
    <div class="brand-mark">
      <span class="brand-mark__main">LUSTRE</span>
      <span class="brand-mark__sub">HAIR ATELIER</span>
    </div>
    <p class="contact contact__name">Kellie-ann Drummond</p>
    <p class="contact contact__phone">0482 736 219</p>
    <p class="contact contact__details">rdw@vomblet.com.au<br>71 Willowmere Rise<br>Corvin Cove NSW 2394</p>
  </section>

  <p class="side-label side-label--back">BACK</p>
  <section class="card card--back" aria-label="Business card back"></section>
</main>
</body>
</html>
```